FotoVELTA buisnesscard

Hey :) I need a modern buisnesscard for my company FotoVELTA
It most have:
Dagligleder og Fotograf: Henrik Torvald Bjelland

Mob: +4791642058
Epost: post@fotovelta.no
Adresse: Bakkestien22, 6090 Fjordvik

Facbook and instagram logo with text FotoVELTA

FotoVELTA logo

It Company

```html
<!DOCTYPE html>
<html lang="no">
<head>
<meta charset="utf-8">
<title>FotoVELTA – visittkort</title>
<link href="https://fonts.googleapis.com/css2?family=Source+Sans+3:wght@400;600;700&display=swap" rel="stylesheet">
<style>
  :root {
    --backdrop: #e9e7e4;
    --card-light: #b4b4b4;
    --card-dark: #050505;
    --ink: #111111;
    --ink-soft: #1c1c1c;
    --silver: #b2b2b2;
    --emboss-light: rgba(0, 0, 0, 0.05);
    --emboss-dark: rgba(255, 255, 255, 0.04);
  }
  * { margin: 0; padding: 0; box-sizing: border-box; }
  html, body { width: 1200px; height: 900px; overflow: hidden; }
  body {
    background: var(--backdrop);
    font-family: "Source Sans 3", "Helvetica Neue", Arial, sans-serif;
    position: relative;
  }
  .card {
    position: absolute;
    overflow: hidden;
    box-shadow: 0 6px 18px rgba(0, 0, 0, 0.18);
  }
  .card--front { left: 78px; top: 35px; width: 587px; height: 363px; background: var(--card-light); color: var(--ink); }
  .card--back { left: 388px; top: 505px; width: 567px; height: 352px; background: var(--card-dark); color: var(--silver); }

  .emboss { position: absolute; border-radius: 50%; }
  .card--front .emboss { left: 150px; top: -40px; width: 360px; height: 360px; border: 28px solid var(--emboss-light); }
  .card--back .emboss { left: 110px; top: -60px; width: 380px; height: 380px; border: 30px solid var(--emboss-dark); }

  .brand {
    position: absolute;
    left: 0; right: 0;
    display: flex;
    flex-direction: column;
    align-items: center;
  }
  .brand__mark { background: currentColor; }
  .brand__name { font-weight: 700; line-height: 1; letter-spacing: 1.5px; white-space: nowrap; }

  .card--front .brand { top: 30px; left: 10px; }
  .card--front .brand__mark { width: 152px; height: 128px; margin-bottom: 12px; }
  .card--front .brand__name { font-size: 70px; }

  .card--back .brand { top: 83px; left: 6px; }
  .card--back .brand__mark { width: 147px; height: 126px; margin-bottom: 10px; }
  .card--back .brand__name { font-size: 68px; }

  .holder {
    position: absolute;
    left: 40px; top: 256px;
    width: 240px;
    text-align: right;
  }
  .holder__name { font-size: 18px; font-weight: 600; line-height: 22px; margin-bottom: 9px; white-space: nowrap; }
  .social { display: flex; justify-content: flex-end; align-items: center; gap: 8px; font-size: 15px; line-height: 21px; }
  .social__badge { width: 12px; height: 12px; background: var(--ink-soft); border-radius: 2px; }

  .divider { position: absolute; left: 294px; top: 270px; width: 1px; height: 60px; background: var(--ink-soft); opacity: 0.6; }

  .contact { position: absolute; left: 311px; top: 260px; list-style: none; font-size: 15.5px; }
  .contact li { display: flex; align-items: center; gap: 6px; height: 22px; white-space: nowrap; }
  .contact li:first-child { margin-bottom: 9px; }
  .contact svg { width: 12px; height: 12px; fill: var(--ink-soft); flex: none; }
</style>
</head>
<body>
  <section class="card card--front">
    <div class="emboss"></div>
    <div class="brand">
      <div class="brand__mark"></div>
      <div class="brand__name">FotoVELTA</div>
    </div>
    <div class="holder">
      <div class="holder__name">Henrik Torvald Bjelland</div>
      <div class="social">FotoVELTA <span class="social__badge"></span></div>
      <div class="social">FotoVELTA <span class="social__badge"></span></div>
    </div>
    <div class="divider"></div>
    <ul class="contact">
      <li>
        <svg viewBox="0 0 12 12"><path d="M6 0a4 4 0 0 0-4 4c0 3 4 8 4 8s4-5 4-8a4 4 0 0 0-4-4zm0 5.6A1.6 1.6 0 1 1 6 2.4a1.6 1.6 0 0 1 0 3.2z"/></svg>
        Bakkestien22, 6090 Fjordvik
      </li>
      <li>
        <svg viewBox="0 0 12 12"><path d="M2.4 0.6 4.2 2.4 3.3 4a7 7 0 0 0 4.7 4.7l1.6-.9 1.8 1.8-1.3 1.8C5 11 1 7 0.6 1.9z"/></svg>
        +4791642058
      </li>
      <li>
        <svg viewBox="0 0 12 12"><path d="M1 2.5h10v7H1z M1 2.5 6 6.5 11 2.5" fill="none" stroke="#1c1c1c" stroke-width="1.4"/></svg>
        post@fotovelta.no
      </li>
    </ul>
  </section>

  <section class="card card--back">
    <div class="emboss"></div>
    <div class="brand">
      <div class="brand__mark"></div>
      <div class="brand__name">FotoVELTA</div>
    </div>
  </section>
</body>
</html>
```